Taking action and overcoming fear with changes in your life. Encouraging people to make a change ...

I need a logo and basic website done in wordpress for my website brightstepforward.example. I would like an image or images showing action and overcoming fear. This is an encouragement site to motivate and inspire. Images showing challenges and overcoming challenges. Bright and exciting. Please use your own creativity.

Font styles to use
Sans Serif

Colors

Designer to choose colors to be used in the design.

```html
<!DOCTYPE html>
<html lang="en">
<head>
<meta charset="utf-8">
<title>Bright Step Forward</title>
<link href="https://fonts.googleapis.com/css2?family=Cinzel:wght@400;700&family=Open+Sans:wght@400;600;700&display=swap" rel="stylesheet">
<style>
:root{
  --brand:#47457f;
  --brand-dark:#3d3b70;
  --ink:#222222;
  --text:#333333;
  --muted:#555555;
  --white:#ffffff;
  --dark:#2d2d2d;
  --bar:#2a2a2a;
  --light:#e7e7e7;
}
*{margin:0;padding:0;box-sizing:border-box}
html,body{width:1200px;height:3240px;overflow:hidden}
body{position:relative;background:var(--white);font-family:'Open Sans',sans-serif;color:var(--text)}
.abs{position:absolute}

/* header */
.site-header{position:absolute;left:0;top:0;width:1200px;height:99px;background:var(--white)}
.brand-mark{left:112px;top:14px;width:75px;height:75px;border-radius:50%;background:var(--brand)}
.brand-name{left:200px;top:36px;font-family:'Cinzel',serif;font-size:27px;font-weight:700;color:var(--brand);letter-spacing:.5px;white-space:nowrap}
.main-nav a{position:absolute;top:45px;font-size:14px;color:#555;text-decoration:none;white-space:nowrap}
.main-nav a.active{color:var(--brand)}
.search-icon{left:1075px;top:47px}

/* hero */
.hero{left:0;top:99px;width:1200px;height:636px;background:linear-gradient(180deg,#6f7479 0%,#8f9499 35%,#7b8085 60%,#5c6166 100%)}
.hero-cut{left:0;top:620px}
.hero-kicker{left:110px;top:200px;font-family:'Cinzel',serif;font-size:45px;color:var(--white);letter-spacing:1px;white-space:nowrap}
.hero-title{left:108px;top:258px;font-family:'Cinzel',serif;font-size:67px;font-weight:700;color:var(--white);white-space:nowrap}
.btn-outline{left:111px;top:367px;width:234px;height:62px;border:2px solid var(--white);border-radius:31px;color:var(--white);font-size:21px;font-weight:600;display:flex;align-items:center;justify-content:center;letter-spacing:.5px}
.dots{left:565px;top:653px;display:flex;gap:4px}
.dots span{width:14px;height:14px;border-radius:50%;border:2px solid var(--white)}
.dots span.on{background:var(--white)}

/* section headings */
.section-title{position:absolute;left:0;width:1200px;text-align:center;font-family:'Cinzel',serif;font-weight:400;white-space:nowrap}
.section-title b{font-weight:700}
.copy{position:absolute;text-align:center;font-size:12.6px;line-height:26.5px;color:var(--text)}
.btn{position:absolute;background:var(--brand);color:var(--white);border-radius:30px;font-weight:700;display:flex;align-items:center;justify-content:center;letter-spacing:.3px}

/* about */
.about{left:0;top:1197px;width:1200px;height:511px;background:radial-gradient(ellipse at 50% 60%,#444 0%,#333 45%,#262626 100%)}

/* services */
.service-card{position:absolute;top:1874px;width:307px}
.service-photo{width:307px;height:181px}
.service-card h3{font-weight:400;font-size:19.5px;color:var(--ink);margin-top:14px}
.service-card p{font-size:11.5px;line-height:21px;color:var(--text);margin-top:8px}
.service-card .btn{position:relative;width:128px;height:38px;font-size:13px;margin-top:24px;border-radius:19px}

/* testimonials */
.testimonials{left:0;top:2316px;width:1200px;height:440px;background:var(--light)}
.avatar{left:223px;top:2443px;width:134px;height:134px;border-radius:50%;border:5px solid var(--white);background:radial-gradient(circle at 50% 45%,#c98a72 0%,#8a3d2c 60%,#5b2418 100%);box-shadow:0 2px 6px rgba(0,0,0,.15)}
.quote{left:394px;top:2471px;width:600px;font-size:16px;line-height:26px;color:var(--ink)}
.quote-name{left:396px;top:2563px;font-size:17px;font-weight:700;font-style:italic;color:var(--brand)}

/* contact */
.contact-band{left:0;top:2680px;width:1200px;height:501px}
.form-title{left:166px;top:2772px;font-family:'Cinzel',serif;font-size:28px;color:var(--white);white-space:nowrap}
.form-title b{font-weight:700}
.form-lead{left:169px;top:2819px;font-size:14px;color:var(--white)}
.field{position:absolute;left:166px;width:396px;border:1px solid rgba(255,255,255,.45);color:var(--white);font-size:13.5px;padding:8px 12px}
.send{left:166px;top:3092px;width:99px;height:38px;border-radius:19px;background:var(--white);color:var(--brand);font-weight:700;font-size:16px;display:flex;align-items:center;justify-content:center}
.contact-title{left:682px;top:2850px;font-family:'Cinzel',serif;font-size:28px;color:var(--white);white-space:nowrap}
.contact-title b{font-weight:700}
.contact-line{position:absolute;left:716px;font-size:14px;line-height:24px;color:var(--white)}
.contact-icon{position:absolute;left:682px}

/* footer */
.site-footer{left:0;top:3181px;width:1200px;height:59px;background:var(--bar)}
.footer-nav a{position:absolute;top:23px;font-size:12px;color:#ddd;text-decoration:none;white-space:nowrap}
.copyright{right:112px;top:23px;font-size:12px;color:#ddd}
</style>
</head>
<body>

<header class="site-header">
  <div class="abs brand-mark"></div>
  <div class="abs brand-name">Bright Step Forward</div>
  <nav class="main-nav">
    <a class="active" style="left:573px">HOME</a>
    <a style="left:650px">ABOUT US</a>
    <a style="left:756px">OUR SERVICES</a>
    <a style="left:888px">BLOG</a>
    <a style="left:961px">CONTACT</a>
  </nav>
  <svg class="abs search-icon" width="14" height="14" viewBox="0 0 14 14"><circle cx="6" cy="6" r="4.3" fill="none" stroke="#444" stroke-width="2"/><line x1="9" y1="9" x2="13" y2="13" stroke="#444" stroke-width="2.2"/></svg>
</header>

<section>
  <div class="abs hero" role="img" aria-label="Woman with umbrella standing on a rocky shore under a stormy sky"></div>
  <svg class="abs hero-cut" width="1200" height="116" viewBox="0 0 1200 116"><polygon points="0,6 25,8 588,115 1157,8 1200,6 1200,116 0,116" fill="#fff"/></svg>
  <div class="abs hero-kicker">ENCOURAGING PEOPLE</div>
  <div class="abs hero-title">TO MAKE A CHANGE</div>
  <div class="abs btn-outline">GET MORE INFO</div>
  <div class="abs dots"><span class="on"></span><span></span><span></span><span></span></div>
</section>

<section>
  <h2 class="section-title" style="top:788px;font-size:37px;color:var(--brand)">WELCOME TO <b>BRIGHT STEP FORWARD</b></h2>
  <p class="copy" style="left:130px;top:852px;width:940px">Sed ut perspiciatis unde omnis iste natus error sit voluptatem accusantium doloremque laudantium, totam rem aperiam, eaque ipsa quae ab illo inventore veritatis et quasi architecto beatae vitae dicta sunt explicabo. Nemo enim ipsam voluptatem quia voluptas sit aspernatur aut odit aut fugit, sed quia consequuntur magni dolores eos qui ratione voluptatem sequi nesciunt.</p>
  <p class="copy" style="left:130px;top:953px;width:940px">At vero eos et accusamus et iusto odio dignissimos ducimus qui blanditiis praesentium voluptatum deleniti atque corrupti quos dolores et quas molestias excepturi sint occaecati cupiditate non provident, similique sunt in culpa qui officia deserunt mollitia animi, id est laborum et dolorum fuga.</p>
  <div class="btn" style="left:502px;top:1051px;width:196px;height:56px;font-size:15px;border-radius:28px">LEARN MORE</div>
</section>

<section>
  <div class="abs about" role="img" aria-label="Dark, muted photo of a lone figure on an empty road"></div>
  <h2 class="section-title" style="top:1288px;font-size:39px;color:var(--white)">ABOUT <b>BRIGHT STEP FORWARD</b></h2>
  <p class="copy" style="left:150px;top:1362px;width:900px;color:#fff;font-size:14px;line-height:32px">But I must explain to you how all this mistaken idea of denouncing pleasure and praising pain was born and I will give you a complete account of the system, and expound the actual teachings of the great explorer of the truth, the master-builder of human happiness.</p>
  <p class="copy" style="left:150px;top:1447px;width:900px;color:#fff;font-size:14px;line-height:32px">At vero eos et accusamus et iusto odio dignissimos ducimus qui blanditiis praesentium voluptatum deleniti atque corrupti quos dolores et quas molestias excepturi sint occaecati cupiditate</p>
  <div class="btn" style="left:508px;top:1560px;width:185px;height:60px;font-size:17px">LEARN MORE</div>
</section>

<section>
  <h2 class="section-title" style="top:1776px;font-size:37px;color:var(--ink)">OUR <b>SERVICES</b></h2>
  <article class="service-card" style="left:122px">
    <div class="service-photo" role="img" aria-label="Silhouettes of people helping each other climb at golden sunset" style="background:linear-gradient(180deg,#c99a3a 0%,#e2b04a 45%,#3a2a10 80%,#111 100%)"></div>
    <h3>Accusantium Doloremque</h3>
    <p>Lorem Ipsum is simply dummy text of the printing and typesetting industry orem scrambled.</p>
    <div class="btn">READ MORE</div>
  </article>
  <article class="service-card" style="left:446px">
    <div class="service-photo" role="img" aria-label="Person leaping from a cliff over the sea at dawn" style="background:linear-gradient(180deg,#4f4a3c 0%,#c9b98f 40%,#e9dcb8 55%,#6c6450 80%,#3c3528 100%)"></div>
    <h3>Praesentium Voluptatum</h3>
    <p>Lorem Ipsum is simply dummy text of the printing and typesetting industry orem scrambled.</p>
    <div class="btn">READ MORE</div>
  </article>
  <article class="service-card" style="left:771px">
    <div class="service-photo" role="img" aria-label="Two smiling older women chatting on a park bench" style="background:linear-gradient(135deg,#2f3a2a 0%,#5b6b4a 40%,#b5603f 65%,#d9c6b0 100%)"></div>
    <h3>Necessitatibus Saepe</h3>
    <p>Lorem Ipsum is simply dummy text of the printing and typesetting industry orem scrambled.</p>
    <div class="btn">READ MORE</div>
  </article>
</section>

<section>
  <div class="abs testimonials"></div>
  <h2 class="section-title" style="top:2390px;font-size:29px;color:var(--ink)">CLIENT <b>TESTIMONIALS</b></h2>
  <svg class="abs" style="left:110px;top:2494px" width="20" height="34" viewBox="0 0 20 34"><polyline points="17,2 3,17 17,32" fill="none" stroke="#555" stroke-width="1.6"/></svg>
  <svg class="abs" style="left:1066px;top:2494px" width="20" height="34" viewBox="0 0 20 34"><polyline points="3,2 17,17 3,32" fill="none" stroke="#555" stroke-width="1.6"/></svg>
  <div class="abs avatar" role="img" aria-label="Portrait of the client giving the testimonial"></div>
  <p class="abs quote">At vero eos et accusamus et iusto odio dignissimos ducimus qui blanditiis praesentium voluptatum deleniti atque corrupti quos dolores et quas molestias excepturi sint occaecati cupiditate non provident.</p>
  <div class="abs quote-name">“Maren”</div>
</section>

<section>
  <svg class="abs contact-band" width="1200" height="501" viewBox="0 0 1200 501" role="img" aria-label="Purple-toned photo of hikers climbing a slope">
    <defs><linearGradient id="bandFill" x1="0" y1="0" x2="1" y2="1"><stop offset="0" stop-color="#4a4884"/><stop offset=".6" stop-color="#45437c"/><stop offset="1" stop-color="#3f3d74"/></linearGradient></defs>
    <polygon points="0,62 583,1 1200,62 1200,501 0,501" fill="url(#bandFill)"/>
  </svg>
  <div class="abs form-title">QUICK SEND US <b>MESSAGE</b></div>
  <div class="abs form-lead">Sed ut perspiciatis unde omnis iste natus error sit voluptatem ...</div>
  <div class="field" style="top:2864px;height:36px">Name</div>
  <div class="field" style="top:2918px;height:36px">Email</div>
  <div class="field" style="top:2969px;height:109px;padding-top:12px">Message</div>
  <div class="abs send">SEND</div>

  <div class="abs contact-title">CONTACT <b>US</b></div>
  <svg class="contact-icon" style="top:2921px" width="12" height="16" viewBox="0 0 12 16"><path d="M6 0C2.7 0 0 2.6 0 5.8 0 10 6 16 6 16s6-6 6-10.2C12 2.6 9.3 0 6 0z" fill="#fff"/><circle cx="6" cy="5.8" r="2.2" fill="#47457f"/></svg>
  <div class="contact-line" style="top:2915px">27 Harbor Lane.<br>Millbrook, 40512.</div>
  <svg class="contact-icon" style="top:2990px" width="14" height="14" viewBox="0 0 14 14"><path d="M3 0l2.5 3-1.5 2c1 2 3 4 5 5l2-1.5L14 11l-2 3C6 14 0 8 0 2z" fill="#fff"/></svg>
  <div class="contact-line" style="top:2986px">1-800 555 0142</div>
  <svg class="contact-icon" style="top:3039px" width="14" height="11" viewBox="0 0 14 11"><rect width="14" height="11" rx="1" fill="#fff"/><polyline points="1,1 7,6 13,1" fill="none" stroke="#47457f" stroke-width="1.3"/></svg>
  <div class="contact-line" style="top:3033px">contact@brightstepforward.example</div>
</section>

<footer class="abs site-footer">
  <nav class="footer-nav">
    <a style="left:114px">HOME</a>
    <a style="left:178px">ABOUT US</a>
    <a style="left:265px">OUR SERVICES</a>
    <a style="left:374px">BLOG</a>
    <a style="left:434px">CONTACT</a>
  </nav>
  <div class="abs copyright">Copyrights © 2019, Company Name. All rights reserved.</div>
</footer>

</body>
</html>
```